Timber Ridge Land Services Business Cards

Need to create a business card with the company logo "Timber Ridge Land Services". The business will provide forestry mulching for land clearing and vegetation control, brush and small tree removal, wildlife habitat improvement and trail and property access creation.

```html
<!DOCTYPE html>
<html lang="en">
<head>
<meta charset="utf-8">
<title>Timber Ridge Land Services — Business Cards</title>
<link rel="stylesheet" href="https://fonts.googleapis.com/css2?family=Montserrat:wght@400;500;700&display=swap">
<style>
  :root {
    --forest: #00634f;
    --forest-deep: #005846;
    --leaf: #6cc46a;
    --paper: #ffffff;
    --backdrop: #3b3b3d;
  }
  * { box-sizing: border-box; margin: 0; padding: 0; }
  html, body {
    width: 1200px; height: 1200px; overflow: hidden;
    background: var(--backdrop);
    font-family: "Montserrat", sans-serif;
  }
  .canvas {
    width: 1200px; height: 1200px;
    display: flex; flex-direction: column; align-items: center; justify-content: center;
    gap: 56px;
  }
  .card {
    width: 760px; height: 434px;
    border-radius: 34px;
    overflow: hidden;
    position: relative;
    box-shadow: 0 14px 30px rgba(0,0,0,0.35);
  }

  /* Front */
  .card-front { background: var(--paper); }
  .front-top {
    position: absolute; left: 0; top: 0; width: 100%; height: 196px;
    display: flex; align-items: center; justify-content: center;
  }
  .accent-band { position: absolute; left: 0; top: 196px; width: 100%; height: 10px; background: var(--leaf); }
  .front-bottom {
    position: absolute; left: 0; top: 214px; width: 100%; height: 220px;
    background: var(--forest);
    display: flex; align-items: center;
  }
  .wordmark {
    text-align: center; font-weight: 700; text-transform: uppercase; line-height: 1.05;
  }
  .wordmark-main { font-size: 46px; letter-spacing: 1px; }
  .wordmark-sub { font-size: 22px; letter-spacing: 3px; }
  .card-front .wordmark { color: var(--forest); }

  .identity { width: 380px; padding-left: 90px; }
  .identity-name { color: var(--leaf); font-size: 42px; font-weight: 500; line-height: 1; letter-spacing: -0.5px; }
  .identity-role { color: var(--paper); font-size: 21px; font-weight: 400; margin-top: 6px; }
  .divider { width: 1px; height: 150px; background: rgba(0,0,0,0.28); }
  .contacts { list-style: none; padding-left: 34px; color: var(--paper); font-size: 16px; line-height: 1.25; }
  .contacts li { display: flex; align-items: flex-start; gap: 10px; margin: 5px 0; }
  .contacts svg { width: 18px; height: 18px; flex: none; margin-top: 1px; }
  .contacts .icon { fill: var(--leaf); stroke: none; }
  .contacts .icon-line { fill: none; stroke: var(--leaf); stroke-width: 1.8; }

  /* Back */
  .card-back {
    background: linear-gradient(160deg, var(--forest) 0%, var(--forest-deep) 100%);
    display: flex; align-items: center; justify-content: center;
  }
  .card-back .wordmark { color: var(--paper); }
  .card-back .wordmark-main { font-size: 58px; }
  .card-back .wordmark-sub { font-size: 28px; }
</style>
</head>
<body>
<main class="canvas">

  <section class="card card-front" aria-label="Business card front">
    <div class="front-top">
      <div class="wordmark">
        <div class="wordmark-main">Timber Ridge</div>
        <div class="wordmark-sub">Land Services</div>
      </div>
    </div>
    <div class="accent-band"></div>
    <div class="front-bottom">
      <div class="identity">
        <div class="identity-name">FULL NAME</div>
        <div class="identity-role">POSITION</div>
      </div>
      <div class="divider"></div>
      <ul class="contacts">
        <li>
          <svg viewBox="0 0 24 24"><path class="icon" d="M6.6 10.8a15.1 15.1 0 0 0 6.6 6.6l2.2-2.2a1 1 0 0 1 1-.25 11.4 11.4 0 0 0 3.6.57 1 1 0 0 1 1 1V20a1 1 0 0 1-1 1A17 17 0 0 1 3 4a1 1 0 0 1 1-1h3.5a1 1 0 0 1 1 1c0 1.25.2 2.45.57 3.57a1 1 0 0 1-.25 1z"/></svg>
          <span>(000) 000 0000</span>
        </li>
        <li>
          <svg viewBox="0 0 24 24"><path class="icon" d="M2 5h20v14H2z"/><path d="M2 5l10 8 10-8" fill="none" stroke="#00634f" stroke-width="1.8"/></svg>
          <span>email@company.com</span>
        </li>
        <li>
          <svg viewBox="0 0 24 24"><circle class="icon-line" cx="12" cy="12" r="9"/><path class="icon-line" d="M3 12h18M12 3c3 3.2 3 14.8 0 18M12 3c-3 3.2-3 14.8 0 18"/></svg>
          <span>www.company.com</span>
        </li>
        <li>
          <svg viewBox="0 0 24 24"><path class="icon" d="M12 2a7 7 0 0 0-7 7c0 5.2 7 13 7 13s7-7.8 7-13a7 7 0 0 0-7-7zm0 9.5A2.5 2.5 0 1 1 12 6.5a2.5 2.5 0 0 1 0 5z"/></svg>
          <span>123 Name Street, 000<br>Your City, 00000-000</span>
        </li>
      </ul>
    </div>
  </section>

  <section class="card card-back" aria-label="Business card back">
    <div class="wordmark">
      <div class="wordmark-main">Timber Ridge</div>
      <div class="wordmark-sub">Land Services</div>
    </div>
  </section>

</main>
</body>
</html>
```